Fun A1 2012 family planner using clever typography and block colour

I have been looking for an A1 2012 family planner and I have not been able to find one. Hence I would like help to develop such a planner. I plan to print it on matt paper, portrait orientated. I have attached some reference pictures of our 2011 planner. I like interesting typography, clear clean colours and simple illustration. I need space to write in daily events and need the weeks and days to be clearly delineated from each other. Each day cell needs the date and day in it (please refer to the file uploaded for a visual reference confirming this). Each weekend needs some kind of colour/ typographic delineation. I want a design for a year-at-a-view calendar. I plan to print the planner in Sydney, Australia with plinthworkprints.com.au and probably to sell printed copies online. The terms & conditions of this project are that I will own the design concept 100% and in perpetuity worldwide once payment has been made. (NB. The attached Work File in Word contains a rough layout and all months, days and dates all typed up to make for quicker design.)

Target Market(s)

Reasonably well heeled family of 4. 2 parents. 2 kids. 2 pets.

Industry/Entity Type

Events

Requirements
Must have
• The calendar must be portrait (not landscape orientated), A1 size. It will be printed on matt paper by plinthworkprints.com.au. It must have months running left to right (Jan-Dec) and day/date cells running top to bottom (refer 2011 planner photos in file uploaded). The day/ date cells must be around 3(w)x2(h)cm - big enough to write daily events in. Weekends must be colour/ typographically delineated. 2012 year must be noted as must "A Lanternmoss Inc Project" and web address in fine print bottom left hand left hand corner.
Nice to have
• A Lanternmoss Inc logo in bottom left hand corder (perhaps Nimble Heron like: http://www.artquarry.com/design_submission.aspx?designid=614307). Header/Footer space for customisation (e.g. "Dunmore-Pratt 2012 Planner" or "XYZ Co 2012 Planner".
Should not have
• The calendar should not use photographs or resemble standard or cheesy wall calendars. No watermarks please.

```html
<!DOCTYPE html>
<html lang="en">
<head>
<meta charset="utf-8">
<title>2012 Planner</title>
<link rel="stylesheet" href="https://fonts.googleapis.com/css2?family=Montserrat:wght@600&family=Oswald:wght@300&family=Poppins:wght@500&display=swap">
<style>
  :root {
    --paper-light: #ffffff;
    --paper-edge: #ececec;
    --ink: #231f20;
    --ink-soft: #555555;
    --ink-light: #ffffff;
    --footer-green: #c9dd5c;
    --jan: #fbb040; --feb: #ef6b35; --mar: #d7df23; --apr: #8dc63f;
    --may: #39b54a; --jun: #009245; --jul: #00aeef; --aug: #2e3192;
    --sep: #ec008c; --oct: #ef4136; --nov: #f15a29; --dec: #f7941d;
  }
  html, body { margin: 0; padding: 0; overflow: hidden; }
  body { width: 847px; height: 1200px; }
  .planner {
    position: relative; width: 847px; height: 1200px; overflow: hidden;
    background: radial-gradient(circle at 62% 50%, var(--paper-light) 0%, #fafafa 45%, var(--paper-edge) 100%);
    font-family: "Oswald", "Arial Narrow", sans-serif; font-weight: 300;
    color: var(--ink-soft);
  }
  .month-bunting { position: absolute; left: 0; top: 0; }
  .month-bunting text {
    font-family: "Montserrat", sans-serif; font-weight: 600;
    font-size: 30px; fill: var(--ink-light);
  }
  .month-days {
    position: absolute; top: 153px; margin: 0; padding: 0; list-style: none;
    --weekend-ink: var(--ink);
  }
  .month-days li {
    width: 24px; height: 23px; margin-bottom: 4.1px;
    display: flex; flex-direction: column; align-items: center; justify-content: center;
    line-height: 1;
  }
  .month-days strong { font-weight: 300; font-size: 11px; }
  .month-days small { font-size: 6px; margin-top: 1px; }
  .month-days .weekend { background: var(--month); color: var(--weekend-ink); }
  .month-jan { left: 57px;  --month: var(--jan); }
  .month-feb { left: 122px; --month: var(--feb); }
  .month-mar { left: 186px; --month: var(--mar); }
  .month-apr { left: 250px; --month: var(--apr); }
  .month-may { left: 315px; --month: var(--may); }
  .month-jun { left: 379px; --month: var(--jun); --weekend-ink: var(--ink-light); }
  .month-jul { left: 444px; --month: var(--jul); }
  .month-aug { left: 508px; --month: var(--aug); --weekend-ink: var(--ink-light); }
  .month-sep { left: 573px; --month: var(--sep); --weekend-ink: var(--ink-light); }
  .month-oct { left: 637px; --month: var(--oct); --weekend-ink: var(--ink-light); }
  .month-nov { left: 701px; --month: var(--nov); }
  .month-dec { left: 766px; --month: var(--dec); }
  .year-block {
    position: absolute; left: 0; top: 1022px; width: 318px; height: 151px;
    background: var(--footer-green); color: var(--ink);
  }
  .year-block .year {
    position: absolute; left: 38px; top: -4px; margin: 0;
    font-family: "Poppins", sans-serif; font-weight: 500; font-size: 112px;
    letter-spacing: -3px; line-height: 1;
  }
  .year-block .project {
    position: absolute; left: 41px; top: 105px; margin: 0;
    font-size: 30px; line-height: 1; letter-spacing: -0.8px;
  }
</style>
</head>
<body>
<main class="planner">
  <svg class="month-bunting" width="847" height="150" viewBox="0 0 847 150" aria-label="Months January to December">
    <g>
      <polygon points="31,137 107,137 69,61" fill="var(--jan)"/>
      <polygon points="96,61 172,61 134,137" fill="var(--feb)"/>
      <polygon points="160,137 236,137 198,61" fill="var(--mar)"/>
      <polygon points="224,61 300,61 262,137" fill="var(--apr)"/>
      <polygon points="289,137 365,137 327,61" fill="var(--may)"/>
      <polygon points="353,61 429,61 391,137" fill="var(--jun)"/>
      <polygon points="418,137 494,137 456,61" fill="var(--jul)"/>
      <polygon points="482,61 558,61 520,137" fill="var(--aug)"/>
      <polygon points="547,137 623,137 585,61" fill="var(--sep)"/>
      <polygon points="611,61 687,61 649,137" fill="var(--oct)"/>
      <polygon points="675,137 751,137 713,61" fill="var(--nov)"/>
      <polygon points="740,61 816,61 778,137" fill="var(--dec)"/>
    </g>
    <g>
      <text transform="translate(44,137) rotate(-56)">Jan</text>
      <text transform="translate(121,120) rotate(-56)">Feb</text>
      <text transform="translate(173,137) rotate(-56)">Mar</text>
      <text transform="translate(249,120) rotate(-56)">Apr</text>
      <text transform="translate(300,137) rotate(-56)">May</text>
      <text transform="translate(377,120) rotate(-56)">Jun</text>
      <text transform="translate(438,137) rotate(-56)">Jul</text>
      <text transform="translate(506,120) rotate(-56)">Aug</text>
      <text transform="translate(559,137) rotate(-56)">Sep</text>
      <text transform="translate(637,120) rotate(-56)">Oct</text>
      <text transform="translate(687,137) rotate(-56)">Nov</text>
      <text transform="translate(765,120) rotate(-56)">Dec</text>
    </g>
  </svg>

  <ol class="month-days month-jan" aria-label="January">
    <li class="weekend"><strong>01</strong><small>SUN</small></li>
    <li><strong>02</strong><small>MON</small></li>
    <li><strong>03</strong><small>TUE</small></li>
    <li><strong>04</strong><small>WED</small></li>
    <li><strong>05</strong><small>THU</small></li>
    <li><strong>06</strong><small>FRI</small></li>
    <li class="weekend"><strong>07</strong><small>SAT</small></li>
    <li class="weekend"><strong>08</strong><small>SUN</small></li>
    <li><strong>09</strong><small>MON</small></li>
    <li><strong>10</strong><small>TUE</small></li>
    <li><strong>11</strong><small>WED</small></li>
    <li><strong>12</strong><small>THU</small></li>
    <li><strong>13</strong><small>FRI</small></li>
    <li class="weekend"><strong>14</strong><small>SAT</small></li>
    <li class="weekend"><strong>15</strong><small>SUN</small></li>
    <li><strong>16</strong><small>MON</small></li>
    <li><strong>17</strong><small>TUE</small></li>
    <li><strong>18</strong><small>WED</small></li>
    <li><strong>19</strong><small>THU</small></li>
    <li><strong>20</strong><small>FRI</small></li>
    <li class="weekend"><strong>21</strong><small>SAT</small></li>
    <li class="weekend"><strong>22</strong><small>SUN</small></li>
    <li><strong>23</strong><small>MON</small></li>
    <li><strong>24</strong><small>TUE</small></li>
    <li><strong>25</strong><small>WED</small></li>
    <li><strong>26</strong><small>THU</small></li>
    <li><strong>27</strong><small>FRI</small></li>
    <li class="weekend"><strong>28</strong><small>SAT</small></li>
    <li class="weekend"><strong>29</strong><small>SUN</small></li>
    <li><strong>30</strong><small>MON</small></li>
    <li><strong>31</strong><small>TUE</small></li>
  </ol>

  <ol class="month-days month-feb" aria-label="February">
    <li><strong>01</strong><small>WED</small></li>
    <li><strong>02</strong><small>THU</small></li>
    <li><strong>03</strong><small>FRI</small></li>
    <li class="weekend"><strong>04</strong><small>SAT</small></li>
    <li class="weekend"><strong>05</strong><small>SUN</small></li>
    <li><strong>06</strong><small>MON</small></li>
    <li><strong>07</strong><small>TUE</small></li>
    <li><strong>08</strong><small>WED</small></li>
    <li><strong>09</strong><small>THU</small></li>
    <li><strong>10</strong><small>FRI</small></li>
    <li class="weekend"><strong>11</strong><small>SAT</small></li>
    <li class="weekend"><strong>12</strong><small>SUN</small></li>
    <li><strong>13</strong><small>MON</small></li>
    <li><strong>14</strong><small>TUE</small></li>
    <li><strong>15</strong><small>WED</small></li>
    <li><strong>16</strong><small>THU</small></li>
    <li><strong>17</strong><small>FRI</small></li>
    <li class="weekend"><strong>18</strong><small>SAT</small></li>
    <li class="weekend"><strong>19</strong><small>SUN</small></li>
    <li><strong>20</strong><small>MON</small></li>
    <li><strong>21</strong><small>TUE</small></li>
    <li><strong>22</strong><small>WED</small></li>
    <li><strong>23</strong><small>THU</small></li>
    <li><strong>24</strong><small>FRI</small></li>
    <li class="weekend"><strong>25</strong><small>SAT</small></li>
    <li class="weekend"><strong>26</strong><small>SUN</small></li>
    <li><strong>27</strong><small>MON</small></li>
    <li><strong>28</strong><small>TUE</small></li>
    <li><strong>29</strong><small>WED</small></li>
  </ol>

  <ol class="month-days month-mar" aria-label="March">
    <li><strong>01</strong><small>THU</small></li>
    <li><strong>02</strong><small>FRI</small></li>
    <li class="weekend"><strong>03</strong><small>SAT</small></li>
    <li class="weekend"><strong>04</strong><small>SUN</small></li>
    <li><strong>05</strong><small>MON</small></li>
    <li><strong>06</strong><small>TUE</small></li>
    <li><strong>07</strong><small>WED</small></li>
    <li><strong>08</strong><small>THU</small></li>
    <li><strong>09</strong><small>FRI</small></li>
    <li class="weekend"><strong>10</strong><small>SAT</small></li>
    <li class="weekend"><strong>11</strong><small>SUN</small></li>
    <li><strong>12</strong><small>MON</small></li>
    <li><strong>13</strong><small>TUE</small></li>
    <li><strong>14</strong><small>WED</small></li>
    <li><strong>15</strong><small>THU</small></li>
    <li><strong>16</strong><small>FRI</small></li>
    <li class="weekend"><strong>17</strong><small>SAT</small></li>
    <li class="weekend"><strong>18</strong><small>SUN</small></li>
    <li><strong>19</strong><small>MON</small></li>
    <li><strong>20</strong><small>TUE</small></li>
    <li><strong>21</strong><small>WED</small></li>
    <li><strong>22</strong><small>THU</small></li>
    <li><strong>23</strong><small>FRI</small></li>
    <li class="weekend"><strong>24</strong><small>SAT</small></li>
    <li class="weekend"><strong>25</strong><small>SUN</small></li>
    <li><strong>26</strong><small>MON</small></li>
    <li><strong>27</strong><small>TUE</small></li>
    <li><strong>28</strong><small>WED</small></li>
    <li><strong>29</strong><small>THU</small></li>
    <li><strong>30</strong><small>FRI</small></li>
    <li class="weekend"><strong>31</strong><small>SAT</small></li>
  </ol>

  <ol class="month-days month-apr" aria-label="April">
    <li class="weekend"><strong>01</strong><small>SUN</small></li>
    <li><strong>02</strong><small>MON</small></li>
    <li><strong>03</strong><small>TUE</small></li>
    <li><strong>04</strong><small>WED</small></li>
    <li><strong>05</strong><small>THU</small></li>
    <li><strong>06</strong><small>FRI</small></li>
    <li class="weekend"><strong>07</strong><small>SAT</small></li>
    <li class="weekend"><strong>08</strong><small>SUN</small></li>
    <li><strong>09</strong><small>MON</small></li>
    <li><strong>10</strong><small>TUE</small></li>
    <li><strong>11</strong><small>WED</small></li>
    <li><strong>12</strong><small>THU</small></li>
    <li><strong>13</strong><small>FRI</small></li>
    <li class="weekend"><strong>14</strong><small>SAT</small></li>
    <li class="weekend"><strong>15</strong><small>SUN</small></li>
    <li><strong>16</strong><small>MON</small></li>
    <li><strong>17</strong><small>TUE</small></li>
    <li><strong>18</strong><small>WED</small></li>
    <li><strong>19</strong><small>THU</small></li>
    <li><strong>20</strong><small>FRI</small></li>
    <li class="weekend"><strong>21</strong><small>SAT</small></li>
    <li class="weekend"><strong>22</strong><small>SUN</small></li>
    <li><strong>23</strong><small>MON</small></li>
    <li><strong>24</strong><small>TUE</small></li>
    <li><strong>25</strong><small>WED</small></li>
    <li><strong>26</strong><small>THU</small></li>
    <li><strong>27</strong><small>FRI</small></li>
    <li class="weekend"><strong>28</strong><small>SAT</small></li>
    <li class="weekend"><strong>29</strong><small>SUN</small></li>
    <li><strong>30</strong><small>MON</small></li>
  </ol>

  <ol class="month-days month-may" aria-label="May">
    <li><strong>01</strong><small>TUE</small></li>
    <li><strong>02</strong><small>WED</small></li>
    <li><strong>03</strong><small>THU</small></li>
    <li><strong>04</strong><small>FRI</small></li>
    <li class="weekend"><strong>05</strong><small>SAT</small></li>
    <li class="weekend"><strong>06</strong><small>SUN</small></li>
    <li><strong>07</strong><small>MON</small></li>
    <li><strong>08</strong><small>TUE</small></li>
    <li><strong>09</strong><small>WED</small></li>
    <li><strong>10</strong><small>THU</small></li>
    <li><strong>11</strong><small>FRI</small></li>
    <li class="weekend"><strong>12</strong><small>SAT</small></li>
    <li class="weekend"><strong>13</strong><small>SUN</small></li>
    <li><strong>14</strong><small>MON</small></li>
    <li><strong>15</strong><small>TUE</small></li>
    <li><strong>16</strong><small>WED</small></li>
    <li><strong>17</strong><small>THU</small></li>
    <li><strong>18</strong><small>FRI</small></li>
    <li class="weekend"><strong>19</strong><small>SAT</small></li>
    <li class="weekend"><strong>20</strong><small>SUN</small></li>
    <li><strong>21</strong><small>MON</small></li>
    <li><strong>22</strong><small>TUE</small></li>
    <li><strong>23</strong><small>WED</small></li>
    <li><strong>24</strong><small>THU</small></li>
    <li><strong>25</strong><small>FRI</small></li>
    <li class="weekend"><strong>26</strong><small>SAT</small></li>
    <li class="weekend"><strong>27</strong><small>SUN</small></li>
    <li><strong>28</strong><small>MON</small></li>
    <li><strong>29</strong><small>TUE</small></li>
    <li><strong>30</strong><small>WED</small></li>
    <li><strong>31</strong><small>THU</small></li>
  </ol>

  <ol class="month-days month-jun" aria-label="June">
    <li><strong>01</strong><small>FRI</small></li>
    <li class="weekend"><strong>02</strong><small>SAT</small></li>
    <li class="weekend"><strong>03</strong><small>SUN</small></li>
    <li><strong>04</strong><small>MON</small></li>
    <li><strong>05</strong><small>TUE</small></li>
    <li><strong>06</strong><small>WED</small></li>
    <li><strong>07</strong><small>THU</small></li>
    <li><strong>08</strong><small>FRI</small></li>
    <li class="weekend"><strong>09</strong><small>SAT</small></li>
    <li class="weekend"><strong>10</strong><small>SUN</small></li>
    <li><strong>11</strong><small>MON</small></li>
    <li><strong>12</strong><small>TUE</small></li>
    <li><strong>13</strong><small>WED</small></li>
    <li><strong>14</strong><small>THU</small></li>
    <li><strong>15</strong><small>FRI</small></li>
    <li class="weekend"><strong>16</strong><small>SAT</small></li>
    <li class="weekend"><strong>17</strong><small>SUN</small></li>
    <li><strong>18</strong><small>MON</small></li>
    <li><strong>19</strong><small>TUE</small></li>
    <li><strong>20</strong><small>WED</small></li>
    <li><strong>21</strong><small>THU</small></li>
    <li><strong>22</strong><small>FRI</small></li>
    <li class="weekend"><strong>23</strong><small>SAT</small></li>
    <li class="weekend"><strong>24</strong><small>SUN</small></li>
    <li><strong>25</strong><small>MON</small></li>
    <li><strong>26</strong><small>TUE</small></li>
    <li><strong>27</strong><small>WED</small></li>
    <li><strong>28</strong><small>THU</small></li>
    <li><strong>29</strong><small>FRI</small></li>
    <li class="weekend"><strong>30</strong><small>SAT</small></li>
  </ol>

  <ol class="month-days month-jul" aria-label="July">
    <li class="weekend"><strong>01</strong><small>SUN</small></li>
    <li><strong>02</strong><small>MON</small></li>
    <li><strong>03</strong><small>TUE</small></li>
    <li><strong>04</strong><small>WED</small></li>
    <li><strong>05</strong><small>THU</small></li>
    <li><strong>06</strong><small>FRI</small></li>
    <li class="weekend"><strong>07</strong><small>SAT</small></li>
    <li class="weekend"><strong>08</strong><small>SUN</small></li>
    <li><strong>09</strong><small>MON</small></li>
    <li><strong>10</strong><small>TUE</small></li>
    <li><strong>11</strong><small>WED</small></li>
    <li><strong>12</strong><small>THU</small></li>
    <li><strong>13</strong><small>FRI</small></li>
    <li class="weekend"><strong>14</strong><small>SAT</small></li>
    <li class="weekend"><strong>15</strong><small>SUN</small></li>
    <li><strong>16</strong><small>MON</small></li>
    <li><strong>17</strong><small>TUE</small></li>
    <li><strong>18</strong><small>WED</small></li>
    <li><strong>19</strong><small>THU</small></li>
    <li><strong>20</strong><small>FRI</small></li>
    <li class="weekend"><strong>21</strong><small>SAT</small></li>
    <li class="weekend"><strong>22</strong><small>SUN</small></li>
    <li><strong>23</strong><small>MON</small></li>
    <li><strong>24</strong><small>TUE</small></li>
    <li><strong>25</strong><small>WED</small></li>
    <li><strong>26</strong><small>THU</small></li>
    <li><strong>27</strong><small>FRI</small></li>
    <li class="weekend"><strong>28</strong><small>SAT</small></li>
    <li class="weekend"><strong>29</strong><small>SUN</small></li>
    <li><strong>30</strong><small>MON</small></li>
    <li><strong>31</strong><small>TUE</small></li>
  </ol>

  <ol class="month-days month-aug" aria-label="August">
    <li><strong>01</strong><small>WED</small></li>
    <li><strong>02</strong><small>THU</small></li>
    <li><strong>03</strong><small>FRI</small></li>
    <li class="weekend"><strong>04</strong><small>SAT</small></li>
    <li class="weekend"><strong>05</strong><small>SUN</small></li>
    <li><strong>06</strong><small>MON</small></li>
    <li><strong>07</strong><small>TUE</small></li>
    <li><strong>08</strong><small>WED</small></li>
    <li><strong>09</strong><small>THU</small></li>
    <li><strong>10</strong><small>FRI</small></li>
    <li class="weekend"><strong>11</strong><small>SAT</small></li>
    <li class="weekend"><strong>12</strong><small>SUN</small></li>
    <li><strong>13</strong><small>MON</small></li>
    <li><strong>14</strong><small>TUE</small></li>
    <li><strong>15</strong><small>WED</small></li>
    <li><strong>16</strong><small>THU</small></li>
    <li><strong>17</strong><small>FRI</small></li>
    <li class="weekend"><strong>18</strong><small>SAT</small></li>
    <li class="weekend"><strong>19</strong><small>SUN</small></li>
    <li><strong>20</strong><small>MON</small></li>
    <li><strong>21</strong><small>TUE</small></li>
    <li><strong>22</strong><small>WED</small></li>
    <li><strong>23</strong><small>THU</small></li>
    <li><strong>24</strong><small>FRI</small></li>
    <li class="weekend"><strong>25</strong><small>SAT</small></li>
    <li class="weekend"><strong>26</strong><small>SUN</small></li>
    <li><strong>27</strong><small>MON</small></li>
    <li><strong>28</strong><small>TUE</small></li>
    <li><strong>29</strong><small>WED</small></li>
    <li><strong>30</strong><small>THU</small></li>
    <li><strong>31</strong><small>FRI</small></li>
  </ol>

  <ol class="month-days month-sep" aria-label="September">
    <li class="weekend"><strong>01</strong><small>SAT</small></li>
    <li class="weekend"><strong>02</strong><small>SUN</small></li>
    <li><strong>03</strong><small>MON</small></li>
    <li><strong>04</strong><small>TUE</small></li>
    <li><strong>05</strong><small>WED</small></li>
    <li><strong>06</strong><small>THU</small></li>
    <li><strong>07</strong><small>FRI</small></li>
    <li class="weekend"><strong>08</strong><small>SAT</small></li>
    <li class="weekend"><strong>09</strong><small>SUN</small></li>
    <li><strong>10</strong><small>MON</small></li>
    <li><strong>11</strong><small>TUE</small></li>
    <li><strong>12</strong><small>WED</small></li>
    <li><strong>13</strong><small>THU</small></li>
    <li><strong>14</strong><small>FRI</small></li>
    <li class="weekend"><strong>15</strong><small>SAT</small></li>
    <li class="weekend"><strong>16</strong><small>SUN</small></li>
    <li><strong>17</strong><small>MON</small></li>
    <li><strong>18</strong><small>TUE</small></li>
    <li><strong>19</strong><small>WED</small></li>
    <li><strong>20</strong><small>THU</small></li>
    <li><strong>21</strong><small>FRI</small></li>
    <li class="weekend"><strong>22</strong><small>SAT</small></li>
    <li class="weekend"><strong>23</strong><small>SUN</small></li>
    <li><strong>24</strong><small>MON</small></li>
    <li><strong>25</strong><small>TUE</small></li>
    <li><strong>26</strong><small>WED</small></li>
    <li><strong>27</strong><small>THU</small></li>
    <li><strong>28</strong><small>FRI</small></li>
    <li class="weekend"><strong>29</strong><small>SAT</small></li>
    <li class="weekend"><strong>30</strong><small>SUN</small></li>
  </ol>

  <ol class="month-days month-oct" aria-label="October">
    <li><strong>01</strong><small>MON</small></li>
    <li><strong>02</strong><small>TUE</small></li>
    <li><strong>03</strong><small>WED</small></li>
    <li><strong>04</strong><small>THU</small></li>
    <li><strong>05</strong><small>FRI</small></li>
    <li class="weekend"><strong>06</strong><small>SAT</small></li>
    <li class="weekend"><strong>07</strong><small>SUN</small></li>
    <li><strong>08</strong><small>MON</small></li>
    <li><strong>09</strong><small>TUE</small></li>
    <li><strong>10</strong><small>WED</small></li>
    <li><strong>11</strong><small>THU</small></li>
    <li><strong>12</strong><small>FRI</small></li>
    <li class="weekend"><strong>13</strong><small>SAT</small></li>
    <li class="weekend"><strong>14</strong><small>SUN</small></li>
    <li><strong>15</strong><small>MON</small></li>
    <li><strong>16</strong><small>TUE</small></li>
    <li><strong>17</strong><small>WED</small></li>
    <li><strong>18</strong><small>THU</small></li>
    <li><strong>19</strong><small>FRI</small></li>
    <li class="weekend"><strong>20</strong><small>SAT</small></li>
    <li class="weekend"><strong>21</strong><small>SUN</small></li>
    <li><strong>22</strong><small>MON</small></li>
    <li><strong>23</strong><small>TUE</small></li>
    <li><strong>24</strong><small>WED</small></li>
    <li><strong>25</strong><small>THU</small></li>
    <li><strong>26</strong><small>FRI</small></li>
    <li class="weekend"><strong>27</strong><small>SAT</small></li>
    <li class="weekend"><strong>28</strong><small>SUN</small></li>
    <li><strong>29</strong><small>MON</small></li>
    <li><strong>30</strong><small>TUE</small></li>
    <li><strong>31</strong><small>WED</small></li>
  </ol>

  <ol class="month-days month-nov" aria-label="November">
    <li><strong>01</strong><small>THU</small></li>
    <li><strong>02</strong><small>FRI</small></li>
    <li class="weekend"><strong>03</strong><small>SAT</small></li>
    <li class="weekend"><strong>04</strong><small>SUN</small></li>
    <li><strong>05</strong><small>MON</small></li>
    <li><strong>06</strong><small>TUE</small></li>
    <li><strong>07</strong><small>WED</small></li>
    <li><strong>08</strong><small>THU</small></li>
    <li><strong>09</strong><small>FRI</small></li>
    <li class="weekend"><strong>10</strong><small>SAT</small></li>
    <li class="weekend"><strong>11</strong><small>SUN</small></li>
    <li><strong>12</strong><small>MON</small></li>
    <li><strong>13</strong><small>TUE</small></li>
    <li><strong>14</strong><small>WED</small></li>
    <li><strong>15</strong><small>THU</small></li>
    <li><strong>16</strong><small>FRI</small></li>
    <li class="weekend"><strong>17</strong><small>SAT</small></li>
    <li class="weekend"><strong>18</strong><small>SUN</small></li>
    <li><strong>19</strong><small>MON</small></li>
    <li><strong>20</strong><small>TUE</small></li>
    <li><strong>21</strong><small>WED</small></li>
    <li><strong>22</strong><small>THU</small></li>
    <li><strong>23</strong><small>FRI</small></li>
    <li class="weekend"><strong>24</strong><small>SAT</small></li>
    <li class="weekend"><strong>25</strong><small>SUN</small></li>
    <li><strong>26</strong><small>MON</small></li>
    <li><strong>27</strong><small>TUE</small></li>
    <li><strong>28</strong><small>WED</small></li>
    <li><strong>29</strong><small>THU</small></li>
    <li><strong>30</strong><small>FRI</small></li>
  </ol>

  <ol class="month-days month-dec" aria-label="December">
    <li class="weekend"><strong>01</strong><small>SAT</small></li>
    <li class="weekend"><strong>02</strong><small>SUN</small></li>
    <li><strong>03</strong><small>MON</small></li>
    <li><strong>04</strong><small>TUE</small></li>
    <li><strong>05</strong><small>WED</small></li>
    <li><strong>06</strong><small>THU</small></li>
    <li><strong>07</strong><small>FRI</small></li>
    <li class="weekend"><strong>08</strong><small>SAT</small></li>
    <li class="weekend"><strong>09</strong><small>SUN</small></li>
    <li><strong>10</strong><small>MON</small></li>
    <li><strong>11</strong><small>TUE</small></li>
    <li><strong>12</strong><small>WED</small></li>
    <li><strong>13</strong><small>THU</small></li>
    <li><strong>14</strong><small>FRI</small></li>
    <li class="weekend"><strong>15</strong><small>SAT</small></li>
    <li class="weekend"><strong>16</strong><small>SUN</small></li>
    <li><strong>17</strong><small>MON</small></li>
    <li><strong>18</strong><small>TUE</small></li>
    <li><strong>19</strong><small>WED</small></li>
    <li><strong>20</strong><small>THU</small></li>
    <li><strong>21</strong><small>FRI</small></li>
    <li class="weekend"><strong>22</strong><small>SAT</small></li>
    <li class="weekend"><strong>23</strong><small>SUN</small></li>
    <li><strong>24</strong><small>MON</small></li>
    <li><strong>25</strong><small>TUE</small></li>
    <li><strong>26</strong><small>WED</small></li>
    <li><strong>27</strong><small>THU</small></li>
    <li><strong>28</strong><small>FRI</small></li>
    <li class="weekend"><strong>29</strong><small>SAT</small></li>
    <li class="weekend"><strong>30</strong><small>SUN</small></li>
    <li><strong>31</strong><small>MON</small></li>
  </ol>

  <footer class="year-block">
    <h1 class="year">2012</h1>
    <p class="project">A Lanternmoss Inc Project</p>
  </footer>
</main>
</body>
</html>
```